依頼詳細
名刺裏面リニューアルのため、裏面のデザインをお願いいたします。
基本的にテキストのみの情報を掲載したいと思っています。
記載項目
①キャッチ
日本で唯一、新規営業に特化した営業支援会社です。

②弊社サービス紹介
・クヌーデル帳:
日本で唯一、新規営業に特化した営業ツール。
営業会社自ら、現場の声と使いやすさをもとにシステムを開発いたしました。

・企業リスト作成:
どんな営業活動も、まずはベストの営業先の見極めから。
社内、そしてWEBのデータを収集・分析を行ない、結果につながる、確度の高い企業リストを作成いたします。

・FAX集客支援:
中小企業、BtoBには非常に有効なFAXの原稿作成、またFAX配信を代行いたします。

③グループ会社一覧(社名の記載のみでかまいません)
・株式会社クレモアリス
・株式会社ミルベーナ
・ポルカノート株式会社
・株式会社ヴェルモンテ
・ハルネス株式会社
・株式会社ロザミオ
・株式会社エピフォルム
・華嶺泰股份有限公司(PELM ON RIVA CO.,LTD)
希望イメージ
シンプル 複雑
単色 カラフル
暗い 明るい
日常 高級
遊び心 厳粛
未来的 伝統的
女性的 男性的
希望する色
黒のテキストを希望します
納品ファイル
• 高解像度JPG (.jpg)
• イラストレーター形式 (.ai)
• フォトショップ形式 (.psd)
• PNG形式 (.png)
補足説明
添付にて参考までに名刺表面と既存の裏面データを送付します
当選者決定後のデータ入稿時ですが、以下の2点をお願いできますでしょうか。
------------------
①文字のアウトライン前のデータと、アウトライン済みのデータの2種類をお送
りください。
②jpg、pdfなどの見本データを一緒にお送りください。
------------------

またデザインにロゴ画像を使用していただいているご提案を当選とさせていただいた際には、
別途ロゴ画像データをお渡しいたしますので、入稿前に調整をお願いさせていただければと思います。
■ 選んだ理由

表面と並べた見たときのバランスの良さが一番のポイントとなりました。
また各コンテンツを読みやすく配置していただいており、営業の現場でもツールとして使いやすいのではないかと思ったことが選択の理由です。

■ 提案者全員のお礼・コメント

このたびは私どもの案件に多くのご提案をいただきありがとうございました。
素晴らしい提案が多く、選定に悩んでしまい、お時間をとってしまい申し訳ありませんでした。

今後もこのようなかたちでコンペを行うこともあるかと思いますが、また機会がありましたらぜひよろしくお願いいたします。

```html
<!DOCTYPE html>
<html lang="ja">
<head>
<meta charset="utf-8">
<title>名刺裏面</title>
<link rel="stylesheet" href="https://fonts.googleapis.com/css2?family=Noto+Sans+JP:wght@400;500;700&display=swap">
<style>
  :root {
    --ink: #1a1a1a;
    --ink-soft: #333333;
    --paper: #ffffff;
    --wash-a: #e4e4e4;
    --wash-b: #f6f6f6;
    --box-a: #e2e2e2;
    --box-b: #f0f0f0;
    --rule: #555555;
  }
  html, body { margin: 0; padding: 0; overflow: hidden; background: var(--paper); }
  .card {
    position: relative;
    width: 766px; height: 1200px;
    overflow: hidden;
    background: var(--paper);
    font-family: "Noto Sans JP", sans-serif;
    color: var(--ink);
  }
  .card-backdrop { position: absolute; inset: 0; }
  .section-label {
    position: absolute; left: 50px; top: 118px; width: 330px;
    font-size: 21px; font-weight: 400; letter-spacing: 1px;
    padding-left: 80px; padding-bottom: 6px;
    border-bottom: 1.5px solid var(--rule);
  }
  .service-title {
    position: absolute; left: 50px;
    display: flex; align-items: center; gap: 12px;
    margin: 0; font-size: 35px; font-weight: 500; letter-spacing: 1px;
  }
  .service-title::before {
    content: ""; width: 26px; height: 26px;
    border: 2.5px solid var(--ink); box-sizing: border-box;
  }
  .service-box {
    position: absolute; left: 50px; width: 435px; box-sizing: border-box;
    padding: 18px 18px 18px 22px;
    border-radius: 16px;
    background: linear-gradient(90deg, var(--box-a), var(--box-b));
    list-style: none; margin: 0;
    font-size: 18px; line-height: 1.7; color: var(--ink-soft);
  }
  .service-box li { position: relative; padding-left: 20px; }
  .service-box li + li { margin-top: 14px; }
  .service-box li::before { content: "•"; position: absolute; left: 0; }
  .catch {
    position: absolute; top: 22px; right: 40px; margin: 0;
    writing-mode: vertical-rl;
    font-size: 55px; font-weight: 500; line-height: 1.65; letter-spacing: 1px;
  }
  .group-label {
    position: absolute; left: 50px; top: 1002px; width: 700px; margin: 0;
    font-size: 21px; font-weight: 400; letter-spacing: 1px;
    padding-left: 370px; box-sizing: border-box;
  }
  .group-label::after {
    content: ""; position: absolute; left: 0; right: 0; bottom: -6px;
    border-bottom: 1.5px solid var(--rule);
  }
  .group-list {
    position: absolute; left: 56px; top: 1048px; width: 690px;
    display: grid; grid-template-columns: 364px 1fr; grid-auto-flow: column;
    grid-template-rows: repeat(4, 37px);
    list-style: none; margin: 0; padding: 0;
    font-size: 20px; color: var(--ink-soft);
  }
  .group-list li::before { content: "• "; }
</style>
</head>
<body>
<main class="card">
  <svg class="card-backdrop" width="766" height="1200" viewBox="0 0 766 1200" aria-hidden="true">
    <defs>
      <linearGradient id="wash" x1="1" y1="0" x2="0" y2="1">
        <stop offset="0" stop-color="var(--wash-a)"/>
        <stop offset="1" stop-color="var(--wash-b)"/>
      </linearGradient>
    </defs>
    <path d="M520 0 L766 0 L766 1200 L0 1200 L0 985 C330 985 520 720 520 0 Z" fill="url(#wash)"/>
  </svg>

  <p class="section-label">弊社サービス紹介</p>

  <h2 class="service-title" style="top:185px">クヌーデル帳</h2>
  <ul class="service-box" style="top:232px">
    <li>日本で唯一、新規営業に特化した営業ツール。</li>
    <li>営業会社自ら、現場の声と使いやすさを<br>もとにシステムを開発いたしました。</li>
  </ul>

  <h2 class="service-title" style="top:505px">企業リスト作成</h2>
  <ul class="service-box" style="top:553px">
    <li>どんな営業活動も、まずはベストの営業先の<br>見極めから。</li>
    <li>社内、そしてwebのデータを収集・分析を行い、<br>結果につながる確度の高い企業リストを<br>作成いたします。</li>
  </ul>

  <h2 class="service-title" style="top:802px">FAX集客支援</h2>
  <ul class="service-box" style="top:850px">
    <li>中小企業、BtoBには非常に有効なFAXの<br>原稿作成、またFAX配信も代行いたします。</li>
  </ul>

  <h1 class="catch">日本で唯一、<br>新規営業に特化した営業支援会社です</h1>

  <h3 class="group-label">グループ会社一覧</h3>
  <ul class="group-list">
    <li>株式会社クレモアリス</li>
    <li>ポルカノート株式会社</li>
    <li>ハルネス株式会社</li>
    <li>株式会社エピフォルム</li>
    <li>華嶺泰股份有限公司</li>
    <li>株式会社ミルベーナ</li>
    <li>株式会社ヴェルモンテ</li>
    <li>株式会社ロザミオ</li>
  </ul>
</main>
</body>
</html>
```